Crestline Gas and Plumbing Business Card Design

I am after a business card design for my plumbing business called 'Crestline Gas & Plumbing'. I do all types of plumbing and gas work and specialise in general maintenance plumbing. Would like to see designs using current logo

Industry/Entity Type

Plumbing

Contact Information for Business Card

Name - Dale Whitcombe
Phone number - 0455163027
Email - admin@crestlinegasandplumbing.example.com.au
ABN - 68204915336

```html
<!DOCTYPE html>
<html lang="en">
<head>
<meta charset="utf-8">
<title>Crestline Gas &amp; Plumbing – Business Card</title>
<link href="https://fonts.googleapis.com/css2?family=PT+Sans:wght@400;700&display=swap" rel="stylesheet">
<style>
  :root {
    --page-bg: #2a2a2a;
    --card-bg: #1c1c1c;
    --emboss: #3a3a3a;
    --emboss-soft: #262626;
    --brand-blue: #2f6fd6;
    --accent-gold: #f2b72b;
    --accent-orange: #e58a2a;
    --text-light: #ececec;
    --icon-blue: #3d6fc4;
  }
  * { box-sizing: border-box; margin: 0; padding: 0; }
  html, body {
    width: 1200px; height: 1200px; overflow: hidden;
    background: var(--page-bg);
    font-family: "PT Sans", sans-serif;
  }
  .canvas { position: relative; width: 1200px; height: 1200px; }
  .card {
    position: absolute; left: 229px; width: 740px; height: 421px;
    background: var(--card-bg);
  }
  .card--front { top: 125px; }
  .card--back { top: 654px; }

  .front-name {
    position: absolute; left: 0; right: 0; top: 180px;
    text-align: center;
    font-weight: 700; font-size: 44px; letter-spacing: 1px;
    text-transform: uppercase;
    color: var(--emboss);
  }

  .abn {
    position: absolute; right: 36px; top: 28px;
    font-size: 15px; color: var(--accent-gold);
  }
  .brand-name {
    position: absolute; left: 44px; top: 84px;
    font-weight: 700; font-size: 32px; line-height: 1.15;
    text-transform: uppercase; color: var(--brand-blue);
  }
  .mark-space {
    position: absolute; left: 470px; top: 95px;
    width: 240px; height: 240px; border-radius: 50%;
    background: var(--emboss-soft);
  }
  .person {
    position: absolute; left: 43px; top: 250px;
  }
  .person__name {
    font-weight: 700; font-size: 22px; color: #fff;
    text-transform: uppercase; letter-spacing: 0.3px;
  }
  .person__role {
    font-size: 16px; color: var(--accent-orange); margin-top: 2px;
  }
  .contact {
    position: absolute; left: 43px; top: 324px;
    list-style: none;
  }
  .contact__item {
    display: flex; align-items: center; gap: 8px;
    font-size: 16px; line-height: 21px; color: var(--text-light);
  }
  .contact__icon { width: 13px; height: 13px; flex: none; }
</style>
</head>
<body>
<main class="canvas">
  <section class="card card--front" aria-label="Card front">
    <p class="front-name">Crestline Gas &amp; Plumbing</p>
  </section>

  <section class="card card--back" aria-label="Card back">
    <p class="abn">ABN - 68204915336</p>
    <p class="brand-name">Crestline<br>Gas &amp; Plumbing</p>

    <div class="mark-space" role="img" aria-label="Embossed brand emblem area"></div>

    <div class="person">
      <p class="person__name">Dale Whitcombe</p>
      <p class="person__role">Manager</p>
    </div>

    <ul class="contact">
      <li class="contact__item">
        <svg class="contact__icon" viewBox="0 0 16 16" aria-hidden="true"><path fill="var(--icon-blue)" d="M3.5 1l2.5 3-1.5 1.8c.9 2 2.6 3.7 4.7 4.7L11 9l3 2.5-1.5 2.8C7 14 2 9 1.7 3.5z"/></svg>
        0455 163 027
      </li>
      <li class="contact__item">
        <svg class="contact__icon" viewBox="0 0 16 16" aria-hidden="true"><rect x="1" y="3" width="14" height="10" fill="var(--icon-blue)"/><path d="M1 3l7 6 7-6" fill="none" stroke="#1c1c1c" stroke-width="1.3"/></svg>
        admin@crestlinegasandplumbing.example.com.au
      </li>
      <li class="contact__item">
        <svg class="contact__icon" viewBox="0 0 16 16" aria-hidden="true"><g fill="none" stroke="var(--icon-blue)" stroke-width="1.2"><circle cx="8" cy="8" r="6.5"/><ellipse cx="8" cy="8" rx="3" ry="6.5"/><path d="M1.5 8h13M2.5 4.5h11M2.5 11.5h11"/></g></svg>
        www.crestlinegasandplumbing.example.com.au
      </li>
    </ul>
  </section>
</main>
</body>
</html>
```